Poster Design

Hello,

My name is Rowan Pickett and I run a vidora channel called 'CrumbleDiary'. I want a poster made for those who watch my video to purchase and put on their wall at home. The poster will be all text and as you can see, I've attached a few examples of posters which I would like it to be similar to. I use a lot of the colour #ab6f7f so it would be good to incorporate this in somewhere (maybe the background colour).
I would like the poster to say:
"Do More Of What Makes YOU Happy"
I need this poster to be for sale ready for christmas, so Im going to need the designs created as soon as possible. Im sorry for the rush.
Have fun with it and feel free to upload multiple versions of a design as well as a few designs if you like.
I look forward to seeing what you come up with.
Rowan
(Of course I will need to own all rights once the payment has been made)

```html
<!DOCTYPE html>
<html lang="en">
<head>
<meta charset="utf-8">
<title>Do More Of What Makes You Happy — Poster</title>
<link rel="stylesheet" href="https://fonts.googleapis.com/css2?family=Oswald:wght@300;400;500;700&display=swap">
<style>
  :root {
    --paper: #ffffff;
    --frame-line: #1a1a1a;
    --poster-black: #000000;
    --sky-top: #c9d6e2;
    --sky-mid: #8fa4b8;
    --meadow: #7a8a4a;
    --flower-pink: #b0455e;
    --flower-green: #4f6b3a;
    --leaf-light: #b7b98a;
    --leaf-dark: #5f6b3c;
    --water-deep: #2f4fb8;
    --water-bright: #5aa8e8;
    --water-pale: #e4f0f8;
    --sand-warm: #d2a87a;
    --sand-cool: #8f948f;
  }
  html, body {
    margin: 0;
    padding: 0;
    width: 1001px;
    height: 1200px;
    overflow: hidden;
    background: var(--paper);
  }
  .canvas {
    position: relative;
    width: 1001px;
    height: 1200px;
    box-sizing: border-box;
    border: 1px solid var(--frame-line);
    background: var(--paper);
  }
  .poster {
    position: absolute;
    left: 111px;
    top: 50px;
    width: 778px;
    height: 1100px;
    background: var(--poster-black);
  }
  .quote {
    margin: 0;
    font-family: "Oswald", "Arial Narrow", sans-serif;
    text-transform: uppercase;
  }
  .quote__line {
    position: absolute;
    left: 0;
    width: 1001px;
    text-align: center;
    line-height: 1;
    white-space: nowrap;
    color: transparent;
    -webkit-background-clip: text;
    background-clip: text;
  }
  .quote__line--do {
    top: 184px;
    font-size: 93px;
    font-weight: 300;
    letter-spacing: -2px;
    background-image: linear-gradient(180deg, var(--sky-top) 0%, var(--sky-mid) 75%, var(--meadow) 100%);
  }
  .quote__line--more {
    top: 315px;
    font-size: 132px;
    font-weight: 300;
    letter-spacing: -4px;
    background-image: linear-gradient(180deg, var(--flower-green) 0%, var(--flower-pink) 45%, var(--flower-green) 100%);
  }
  .quote__line--of-what {
    top: 482px;
    font-size: 130px;
    font-weight: 400;
    letter-spacing: -5px;
    word-spacing: -18px;
    background-image: linear-gradient(160deg, var(--leaf-light) 0%, var(--leaf-dark) 55%, var(--leaf-light) 100%);
  }
  .quote__line--makes-you {
    top: 649px;
    font-size: 130px;
    font-weight: 500;
    letter-spacing: -5px;
    word-spacing: -14px;
    background-image: linear-gradient(90deg, var(--water-deep) 0%, var(--water-bright) 55%, var(--water-pale) 100%);
  }
  .quote__line--happy {
    top: 804px;
    font-size: 257px;
    font-weight: 700;
    letter-spacing: -6px;
    transform: scaleX(0.86);
    transform-origin: 500px 0;
    background-image: linear-gradient(100deg, var(--sand-warm) 0%, var(--sand-warm) 45%, var(--sand-cool) 100%);
  }
</style>
</head>
<body>
  <main class="canvas">
    <div class="poster"></div>
    <h1 class="quote">
      <span class="quote__line quote__line--do">Do</span>
      <span class="quote__line quote__line--more">More</span>
      <span class="quote__line quote__line--of-what">Of What</span>
      <span class="quote__line quote__line--makes-you">Makes You</span>
      <span class="quote__line quote__line--happy">Happy</span>
    </h1>
  </main>
</body>
</html>
```